Post Card Mailer for QUIK PATH PROSPECTS using new logo

We need a post card designed to send through the USA mail service that will go to new prospective clients.

The post card will introduce me and my new company and try to educate them our on company and services.

The goal is for them to call me or email me so I can have a discussion and try to sell our product.

Our product is a name list of individuals that are looking for consulting / help to determine if they qualify for USA social security benefits and then help to manage the process. We sell this name list to law firms that help these individuals.

Our services are better because we have a better less expensive way to identify people via the internet that want help. Our conversion rate is 15%, so every 100 leads a law firm buys the will obtain 15 customers / clients.

Designer on Logo took alot longer than expected. Also there were two projects that needed to combined into one. Which was done yesterday.

Target Market(s)

Law firms

Font styles to use
Serif
Sans Serif
Script

Colors

Designer to choose colors to be used in the design.

Requirements
Must have
• The size of the mailer should be about 6 by 8 inches.
• Two sides.
• Side 1: With our Logo and key messages we want to communicate.
• Side 2: A space to be used by the USA mail services in lower right, my photo and an introduction by me to our company and why they should buy from my company.
Nice to have
• Images that represent what we do, how we help, and our target market.
Should not have
• Poor taste in images that upset people

```html
<!DOCTYPE html>
<html lang="en">
<head>
<meta charset="utf-8">
<title>Quik Path Prospects – Postcard Mailer</title>
<link href="https://fonts.googleapis.com/css2?family=Open+Sans:ital,wght@0,400;0,600;0,700;1,600&display=swap" rel="stylesheet">
<style>
:root{
  --page:#e9e9ec;
  --royal:#0a5fd6;
  --cyan:#17b6f2;
  --ocean:#0e78c4;
  --ink:#26323f;
  --night:#1b222c;
  --slate:#3c4656;
  --link:#1366b5;
  --white:#ffffff;
  --text:#2a3b55;
}
*{margin:0;padding:0;box-sizing:border-box}
html,body{width:1200px;height:1200px;overflow:hidden}
body{background:var(--page);font-family:"Open Sans",Arial,sans-serif;position:relative}

/* ---------- Front side ---------- */
.front{position:absolute;left:270px;top:32px;width:660px;height:494px;background:var(--royal);overflow:hidden}
.front-hero{position:absolute;left:0;top:0;width:660px;height:277px;background:linear-gradient(120deg,var(--night) 0%,#2a3340 55%,#525c6a 100%)}
.front-brand{position:absolute;left:0;top:128px;width:660px;text-align:center;color:var(--white);font-weight:700;font-size:38px;letter-spacing:2px}
.feature{position:absolute;top:225px;width:170px;margin-left:-85px;text-align:center;color:var(--white)}
.feature-icon{width:104px;height:104px;margin:0 auto;border-radius:50%;background:var(--cyan);border:4px solid var(--white);display:flex;align-items:center;justify-content:center}
.feature-title{margin-top:14px;font-size:14px;font-weight:700;letter-spacing:.8px;line-height:20px}
.feature-text{margin-top:7px;font-size:12px;line-height:20.5px;letter-spacing:.3px}
.feature-text.strong{font-weight:600}

/* ---------- Back side ---------- */
.back{position:absolute;left:274px;top:601px;width:652px;height:489px;background:var(--white);overflow:hidden}
.intro{position:absolute;left:0;top:0;width:258px;height:489px;background:var(--ocean);color:var(--white)}
.portrait{position:absolute;left:63px;top:32px;width:126px;height:126px;border-radius:50%;background:radial-gradient(circle at 50% 40%,#c9a99a 0%,#7d6a66 45%,#3a3e48 100%)}
.intro-name{position:absolute;left:0;top:160px;width:258px;text-align:center;font-size:26px;font-weight:700;letter-spacing:.5px}
.intro-role{position:absolute;left:0;top:190px;width:258px;text-align:center;font-size:13px;font-style:italic;font-weight:600}
.intro-body{position:absolute;left:20px;top:245px;width:228px;font-size:9px;line-height:10.8px;font-weight:600}
.intro-body .lead{font-size:13.5px;font-weight:700;line-height:17px;letter-spacing:.4px}
.intro-body .close{font-size:11.5px;font-weight:700;line-height:14px}
.intro-body .close small{font-size:9px}

.back-brand{position:absolute;left:258px;top:50px;width:394px;text-align:center;color:var(--link);font-size:25px;font-weight:700;letter-spacing:1px}
.tagline{position:absolute;left:270px;top:128px;width:370px;text-align:center;color:var(--link);font-size:11.5px;font-weight:700;line-height:14px;letter-spacing:.3px}
.offer-rule{position:absolute;left:258px;top:220px;width:394px;height:3px;background:var(--link)}
.offer{position:absolute;left:258px;top:223px;width:394px;height:84px;background:var(--ink);text-align:center;font-weight:700;letter-spacing:.5px}
.offer p{font-size:11.5px;line-height:18px}
.offer .hi{color:var(--cyan)}
.offer .lo{color:var(--white)}
.offer .first{margin-top:28px}
.offer-pill{position:absolute;left:359px;top:208px;width:186px;height:30px;border:2px solid var(--link);border-radius:15px;background:var(--white);color:var(--link);font-size:14px;font-weight:700;letter-spacing:1px;text-align:center;line-height:26px}
.sender{position:absolute;left:274px;top:324px;color:var(--text);font-size:11.5px;line-height:13.7px;letter-spacing:.4px}
.recipient{position:absolute;left:274px;top:412px;color:var(--text);font-size:11.5px;letter-spacing:.4px}
.dotline{position:absolute;left:274px;height:0;border-top:1px dotted var(--text)}
.stamp{position:absolute;left:560px;top:397px;width:76px;height:76px;border:1px solid #dcdcdc;background:var(--white)}
</style>
</head>
<body>

<section class="front">
  <div class="front-hero" role="img" aria-label="Dimly lit modern office interior behind the company name"></div>
  <div class="front-brand">QUIK PATH PROSPECTS</div>

  <div class="feature" style="left:76px">
    <div class="feature-icon">
      <svg width="60" height="44" viewBox="0 0 60 44" fill="none" stroke="#fff" stroke-width="5" stroke-linecap="round" stroke-linejoin="round"><polyline points="4,38 20,24 30,30 52,10"/><polyline points="40,8 54,8 54,22"/></svg>
    </div>
    <div class="feature-title">HIGH VOLUME,<br>QUALITY LEADS</div>
    <div class="feature-text">50 years of SSD domain<br>knowledge Tested<br>technology capabilities</div>
  </div>

  <div class="feature" style="left:251px">
    <div class="feature-icon">
      <svg width="50" height="60" viewBox="0 0 50 60" fill="#fff"><circle cx="25" cy="22" r="19"/><circle cx="25" cy="22" r="13" fill="#17b6f2"/><polygon points="25,13 27.6,19.5 34,19.8 29,24 30.6,30.5 25,27 19.4,30.5 21,24 16,19.8 22.4,19.5"/><polygon points="14,36 8,56 16,52 20,58 25,40"/><polygon points="36,36 42,56 34,52 30,58 25,40"/></svg>
    </div>
    <div class="feature-title">BEST LEADS,<br>BEST PRICE</div>
    <div class="feature-text">Our high conversation<br>rates lowers your client<br>acquisition cost<br>Referrals available</div>
  </div>

  <div class="feature" style="left:410px">
    <div class="feature-icon">
      <svg width="56" height="50" viewBox="0 0 56 50" fill="none" stroke="#fff" stroke-width="4"><rect x="4" y="4" width="48" height="42" rx="3"/><line x1="4" y1="25" x2="40" y2="25"/><polyline points="34,18 42,25 34,32"/><line x1="18" y1="4" x2="18" y2="16"/><line x1="32" y1="34" x2="32" y2="46"/></svg>
    </div>
    <div class="feature-title">EZ<br>TO USE</div>
    <div class="feature-text">Integrate seamlessly into<br>your IT systems<br>Tailored campaigns</div>
  </div>

  <div class="feature" style="left:580px">
    <div class="feature-icon">
      <svg width="52" height="42" viewBox="0 0 52 42" fill="none" stroke="#fff" stroke-width="6" stroke-linecap="round" stroke-linejoin="round"><polyline points="6,22 20,36 46,8"/></svg>
    </div>
    <div class="feature-title">TRUSTED<br>PARTNER</div>
    <div class="feature-text strong">Reliability, Dependable,<br>Helpful Deep business &amp;<br>process acumen</div>
  </div>
</section>

<section class="back">
  <div class="intro">
    <div class="portrait" role="img" aria-label="Portrait photo of the company president"></div>
    <div class="intro-name">Marcus Delling</div>
    <div class="intro-role">President, Quik Path Prospects</div>
    <div class="intro-body">
      <p class="lead">I want to personally introduce our company to you!</p>
      <p>My team as &gt; 50 years of cumulative SSD experience.</p>
      <p>We have proven technology that delivers the best leads.</p>
      <p>The timing is right for a new competitor in this industry.</p>
      <p>I had to come out of retirement after 30 years with Norvell Industries, the opportunity is just that great … I love building businesses and partnering with great customers!</p>
      <p>Our business, industry, &amp; technical acumen is unrivaled … and we can do it at a cost than no others can.</p>
      <p class="close"><small>Let’s work together to bring Social Security</small><br>Disability benefits to those in need and deserving!</p>
    </div>
  </div>

  <div class="back-brand">QUIK PATH PROSPECTS</div>
  <p class="tagline">Best Leads … Best Price with High Volume &amp; Quality capacity … Leads from a Trusted Partner that is EZ to use</p>

  <div class="offer-rule"></div>
  <div class="offer">
    <p class="hi first">START AT 250 OR 500 LEADS</p>
    <p class="lo">GROW TO 1,000 … 3,000 OR EVEN 10,000!</p>
    <p class="hi">WE GIVE THE RIGHT SUPPORT TO YOUR GROWTH.</p>
  </div>
  <div class="offer-pill">TEST OUR LEADS</div>

  <address class="sender" style="font-style:normal">
    Marcus Delling, President Quik Path Prospects<br>
    2150 Harlow Avenue, Suite 400<br>
    Dayton Ohio OH 45402<br>
    555-014-2290<br>
    Marcus@QuikPathProspects.com
  </address>
  <div class="recipient">To:&nbsp; Addressee</div>
  <div class="dotline" style="top:440px;width:256px"></div>
  <div class="dotline" style="top:456px;width:256px"></div>
  <div class="dotline" style="top:471px;width:140px"></div>
  <div class="stamp"></div>
</section>

</body>
</html>
```